Bright Harbor Capital website

Build a website template for the Bright Harbor Capital fund.
Looking for a cool website design showing companies we are using the latest in web design trends. We want to attract app developers, typically the younger set.
A good example of one of our competitive firms is http://tallmeadowfund.example
The required components for the website include:
1) Funding application
2) about our firm
a) Partner profiles - We will include photographs and bios about each of the partners in our firm.
b) Invest with Bright Harbor - This will include information how to invest with our fund
c) our process - About our process for evaluating, funding and helping build successful businesses - This will include a narrative about the target companies, how we work, the type of deals we are interested in, our expectations, etc ...
3) Investment profiles - Stories about the companies we invest with
4) News - Output from our twitter feed and copies of our Blog posts

```html
<!DOCTYPE html>
<html lang="en">
<head>
<meta charset="utf-8">
<title>Bright Harbor Capital</title>
<link href="https://fonts.googleapis.com/css2?family=Mulish:wght@300;400;600&display=swap" rel="stylesheet">
<style>
  :root{
    --green:#5a9a0c;
    --green-dark:#3f7a06;
    --ink:#4a4a4a;
    --body:#6a6a6a;
    --rule:#cfcfcf;
    --panel:#f6f4f4;
    --band:#f1f1f1;
    --hero-a:#d9d9d9;
    --hero-b:#c4c4c4;
    --sky:#1d7fa8;
  }
  *{box-sizing:border-box;margin:0;padding:0}
  html,body{width:856px;height:1200px;overflow:hidden;background:#fff}
  body{position:relative;font-family:"Mulish",Arial,sans-serif;color:var(--body)}
  .abs{position:absolute}

  /* header + hero */
  .hero{left:0;top:0;width:856px;height:315px;background:linear-gradient(100deg,var(--hero-a),#e8e8e8 40%,var(--hero-b))}
  .hero-photo{left:330px;top:50px;width:526px;height:265px;background:linear-gradient(90deg,rgba(220,220,220,0),#a9a9a9 45%,#6b6b6b 75%,#bcbcbc)}
  .topbar{left:0;top:0;width:856px;height:50px;background:#fff;border-bottom:2px solid #bdbdbd}
  .logo-panel{left:0;top:0}
  .brand{left:102px;top:34px;display:flex;align-items:center;gap:8px;font-size:21px;font-weight:600;color:var(--green)}
  .brand-dot{width:30px;height:30px;border-radius:50%;background:var(--green)}
  .nav{left:374px;top:21px;display:flex;gap:10px;font-size:8px;color:var(--ink);text-transform:uppercase;letter-spacing:-.1px}
  .welcome{right:563px;top:163px;text-align:right}
  .welcome h1{font-size:20px;font-weight:400;color:var(--green);margin-bottom:2px}
  .welcome p{font-size:12.5px;line-height:15px;color:var(--ink)}
  .dots{left:259px;top:228px;display:flex;gap:4px}
  .dots span{width:8px;height:8px;background:#8a8a8a}
  .dots span:first-child{background:var(--green)}

  /* headings */
  .h2{font-size:14.5px;font-weight:400;color:var(--ink);display:flex;align-items:center;gap:12px}
  .h2 em{font-style:normal;color:var(--green)}
  .h2 .dash{flex:1;height:3px;border-top:1px dotted var(--rule);border-bottom:1px dotted var(--rule)}

  /* feature cards */
  .card{left:104px;width:409px;height:124px;border:1px solid #e4e4e4;padding:4px}
  .card-inner{display:flex;height:100%;background:var(--panel)}
  .card-img{width:160px;height:114px;flex:none}
  .card-body{padding:10px 16px 0 16px}
  .card-body h3{font-size:11.5px;font-weight:400;color:var(--ink);margin-bottom:5px}
  .card-body p{font-size:10.5px;line-height:14px;color:var(--body)}
  .more{font-size:10px;color:var(--green);margin-top:6px;display:block}

  /* form */
  .field{left:533px;width:223px;border:1px solid #c9c9c9;font-size:11px;color:var(--body);padding:9px 7px}
  .submit{left:533px;top:538px;width:74px;height:32px;background:linear-gradient(#5da10d,#3f7f06);color:#fff;font-size:11.5px;display:flex;align-items:center;justify-content:center}
  .rule{left:533px;top:592px;width:223px;border-top:1px dashed var(--rule)}

  /* partners */
  .partner{left:533px;width:223px;display:flex;gap:8px}
  .partner-img{width:58px;height:48px;flex:none;background:linear-gradient(#bfb7a6,#6c6658)}
  .partner p{font-size:8.3px;line-height:13.5px;color:var(--body)}
  .partner b{font-weight:400;color:var(--green)}
  .partner i{font-style:normal;color:var(--ink)}

  .inv{top:803px;width:68px;height:68px;border:1px solid #d6d6d6;padding:2px}
  .inv div{width:100%;height:100%;background:radial-gradient(#fff 40%,#d4d4d4);display:flex;align-items:center;justify-content:center;font-size:10px;font-weight:600;color:var(--ink)}

  /* blog band */
  .band{left:0;top:906px;width:856px;height:228px;background:var(--band)}
  .post{left:104px;width:409px;display:flex;gap:12px}
  .date{width:50px;height:50px;flex:none;background:var(--green-dark);border:2px solid #e2e2e2;outline:1px solid #cfcfcf;color:#fff;text-align:center;padding-top:7px}
  .date b{display:block;font-size:15px;font-weight:400;line-height:16px}
  .date span{font-size:9px}
  .post h4{font-size:8.5px;font-weight:400;color:var(--green);margin-bottom:3px}
  .post p{font-size:8px;line-height:12.5px}
  .post i{font-style:normal;color:var(--ink);font-size:8px}

  .tweet{left:533px;top:930px;width:224px;height:170px;background:#fff;border:1px solid #e0e0e0;padding:12px}
  .tweet h3{font-size:13.5px;font-weight:400;color:var(--ink);padding-bottom:8px;border-bottom:1px dashed var(--rule)}
  .follow{display:flex;gap:8px;margin-top:11px;font-size:9.5px;color:var(--ink);line-height:17px}
  .follow-sq{width:31px;height:31px;background:var(--sky)}
  .follow u{color:var(--ink)}
  .faces{display:flex;gap:7px;margin-top:10px}
  .faces div{width:64px;height:63px}

  .footer{left:104px;top:1160px;display:flex;gap:13px;font-size:8px;color:var(--ink)}
  .copy{left:626px;top:1160px;font-size:8px;color:var(--ink)}
  .copy em{font-style:normal;color:var(--green)}
</style>
</head>
<body>

<header>
  <div class="abs hero"></div>
  <div class="abs hero-photo" role="img" aria-label="Photo of a smiling businessman in a suit with two colleagues working at a laptop behind him"></div>
  <div class="abs topbar"></div>
  <svg class="abs logo-panel" width="370" height="102" viewBox="0 0 370 102">
    <polygon points="0,0 368,0 293,101 0,101" fill="#fafafa"/>
    <polyline points="368,0 293,101 0,101" fill="none" stroke="#dcdcdc" stroke-width="1.5"/>
  </svg>
  <div class="abs brand"><span class="brand-dot"></span>Bright Harbor Capital</div>
  <nav class="abs nav">
    <span>Funding Application</span><span>About Us</span><span>Invest with us</span><span>Partners</span><span>Process</span><span>Profiles</span><span>News</span>
  </nav>
  <div class="abs welcome">
    <h1>Welcome to our site</h1>
    <p>Evaluating, funding and helping<br>build successful businesses</p>
  </div>
  <div class="abs dots"><span></span><span></span><span></span></div>
</header>

<main>
  <div class="abs h2" style="left:104px;top:354px;width:409px"><span><em>About</em> Us</span><span class="dash"></span></div>
  <div class="abs card" style="top:386px">
    <div class="card-inner">
      <div class="card-img" role="img" aria-label="Sepia portrait of a man in a coat" style="background:linear-gradient(#e6e1d6,#8a7a62)"></div>
      <div class="card-body">
        <h3>Know who we are</h3>
        <p>Lorem ipsum dolor sit amet, consectetur adipisicing elit, sed do eiusmod tempor incididunt ut labore et dolore magna aliqua.</p>
        <span class="more">Read More &gt;</span>
      </div>
    </div>
  </div>

  <div class="abs h2" style="left:104px;top:538px;width:409px"><span><em>Invest with</em> Bright Harbor</span><span class="dash"></span></div>
  <div class="abs card" style="top:566px">
    <div class="card-inner">
      <div class="card-img" role="img" aria-label="Hands reviewing financial charts with a pen and tablet" style="background:linear-gradient(135deg,#2c3a52,#d9e2ec 50%,#3a7fc1)"></div>
      <div class="card-body">
        <h3>How to invest with our fund</h3>
        <p>Lorem ipsum dolor sit amet, consectetur adipisicing elit, sed do eiusmod tempor incididunt ut labore et dolore magna aliqua.</p>
        <span class="more">Read More &gt;</span>
      </div>
    </div>
  </div>

  <div class="abs h2" style="left:104px;top:719px;width:409px"><span><em>Investment</em>&nbsp; Process</span><span class="dash"></span></div>
  <div class="abs card" style="top:747px">
    <div class="card-inner">
      <div class="card-img" role="img" aria-label="Laptop showing a bar chart on a meeting table" style="background:linear-gradient(135deg,#6e5a44,#b8b2a6 50%,#3d3b38)"></div>
      <div class="card-body">
        <h3>3 step process to investment</h3>
        <p>Lorem ipsum dolor sit amet, consectetur adipisicing elit, sed do eiusmod tempor incididunt ut labore et dolore magna aliqua.</p>
        <span class="more">Read More &gt;</span>
      </div>
    </div>
  </div>

  <aside>
    <div class="abs h2" style="left:533px;top:354px"><span><em>Request for</em> Financing</span></div>
    <div class="abs field" style="top:385px;height:32px">Name</div>
    <div class="abs field" style="top:422px;height:33px">Email id</div>
    <div class="abs field" style="top:460px;height:68px">Query</div>
    <div class="abs submit">Submit</div>
    <div class="abs rule"></div>

    <div class="abs h2" style="left:533px;top:607px"><span><em>Partner</em> Profiles</span></div>
    <div class="abs partner" style="top:634px">
      <div class="partner-img" role="img" aria-label="Partner portrait photo"></div>
      <p><b>Owen Carraway,</b><br>We will include photographs and bios about each of the partners in our firm. <i>Read More &gt;&gt;</i></p>
    </div>
    <div class="abs partner" style="top:700px">
      <div class="partner-img" role="img" aria-label="Partner portrait photo"></div>
      <p><b>Owen Carraway,</b><br>We will include photographs and bios about each of the partners in our firm. <i>Read More &gt;&gt;</i></p>
    </div>

    <div class="abs h2" style="left:533px;top:774px"><span><em>Investment</em> Profiles</span></div>
    <div class="abs inv" style="left:534px"><div>Voltrix</div></div>
    <div class="abs inv" style="left:610px"><div>Tradelane</div></div>
    <div class="abs inv" style="left:686px"><div>Keyform</div></div>
  </aside>
</main>

<section>
  <div class="abs band"></div>
  <div class="abs h2" style="left:104px;top:939px"><span>Our Blog</span></div>
  <div class="abs" style="left:104px;top:968px;width:409px;border-top:1px dashed var(--rule)"></div>
  <div class="abs post" style="top:984px">
    <div class="date"><b>12</b><span>JAN</span></div>
    <div>
      <h4>Blog headline1</h4>
      <p>Lorem ipsum dolor sit amet, consectetur adipisicing elit, sed do eiusmod tempor incididunt ut labore et dolore magna aliqua.</p>
      <i>Read Details &gt;</i>
    </div>
  </div>
  <div class="abs post" style="top:1050px">
    <div class="date"><b>26</b><span>JAN</span></div>
    <div>
      <h4>Blog headline2</h4>
      <p>Lorem ipsum dolor sit amet, consectetur adipisicing elit, sed do eiusmod tempor incididunt ut labore et dolore magna aliqua.</p>
      <i>Read Details &gt;</i>
    </div>
  </div>

  <div class="abs tweet">
    <h3>Tweet Us</h3>
    <div class="follow">
      <div class="follow-sq"></div>
      <div>31213 Followers<br>
        <svg width="9" height="9" viewBox="0 0 10 10" style="vertical-align:-1px"><rect x="0" y="4" width="2.5" height="6" fill="#1d7fa8"/><path d="M3.5 4 L6 0.5 Q7 0.5 6.8 2.5 L6.5 4 H9.5 L8.5 10 H3.5 Z" fill="#1d7fa8"/></svg>
        <u>Tweet Us</u></div>
    </div>
    <div class="faces">
      <div role="img" aria-label="Follower photo: man on a phone" style="background:linear-gradient(#d8d2cc,#7a6256)"></div>
      <div role="img" aria-label="Follower photo: smiling man" style="background:linear-gradient(#c9ccd2,#4d5460)"></div>
      <div role="img" aria-label="Follower photo: smiling woman" style="background:linear-gradient(#d9eef2,#4a3228)"></div>
    </div>
  </div>
</section>

<footer>
  <div class="abs footer"><span>Funding application</span><span>About Us</span><span>Invest with us</span><span>Partners</span><span>process</span><span>profiles</span><span>News</span></div>
  <div class="abs copy">Copyright@2014, <em>Bright Harbor</em></div>
</footer>

</body>
</html>
```